redesign corporate website (software courses)

We need a complete redesign of the current website: http://q-o-r.biz/ (training: http://q-o-r.biz/pt-br/treinamento/web ); more clear, different color, navigation, header, footer, whatever (side note: site will be based on bootstrap and drupal). Most important pages:

http://q-o-r.biz/pt-br/treinamento (trainingoverviewpage)
http://q-o-r.biz/ (frontpage)
http://q-o-r.biz/pt-br/treinamento/web (trianingdetailpage)

The design should be valid for further content pages (like http://q-o-r.biz/pt-br/desenvolvimentodesoftware) and pages with forms (http://q-o-r.biz/pt-br/contact or http://q-o-r.biz/pt-br/training/web/register)

Logo attached in white and black and black with shadow.

Some other examples of training sites (just content examples - not as template for similar layout):

http://www.brivatutor.example/packages/4817/Website-Development-Professional-training.html?advid=31&gclid=XQa93pLmw42HGtrk5BsjEZWKpR
http://www.code-lehrhaus.example/
http://www.devalto.example/cursos/kestrel-framework-ii/
http://www.varnholt-academy.example/lp/php-development-training.aspx?gclid=MT3hwqUvb52DJYRR8Bpexk9B7B

Industry/Entity Type

Software

```html
<!DOCTYPE html>
<html lang="en">
<head>
<meta charset="utf-8">
<title>Qoral Software Institute</title>
<link href="https://fonts.googleapis.com/css2?family=Figtree:wght@300;400;600;700&family=Open+Sans:wght@400;600&display=swap" rel="stylesheet">
<style>
:root{
  --ink:#2b2b2b;
  --muted:#8a8a8a;
  --accent:#e4401b;
  --green:#5ccd2f;
  --sky:#49b9e0;
  --teal-muted:#8fb0b8;
  --topbar:#1c1c1c;
  --footer:#141414;
  --panel:#f6f6f6;
  --line:#e4e4e4;
  --dark-btn:#434848;
  --white:#ffffff;
}
*{margin:0;padding:0;box-sizing:border-box}
html,body{width:684px;height:1200px;overflow:hidden;background:var(--white)}
body{position:relative;font-family:"Figtree",Arial,sans-serif;color:var(--ink)}
.abs{position:absolute}

/* top bar */
.topbar{position:absolute;left:0;top:0;width:684px;height:22px;background:var(--topbar);display:flex;justify-content:flex-end;align-items:center;gap:12px;padding-right:64px;font-size:5.6px;font-weight:600;color:#ddd;letter-spacing:.1px}
.topbar span{display:flex;align-items:center;gap:3px}
.topbar .call{color:var(--accent)}
.topbar svg{width:7px;height:7px}

/* header */
.header{position:absolute;top:22px;left:0;width:684px;height:40px;background:var(--white)}
.brand{position:absolute;left:66px;top:8px;display:flex;align-items:center;gap:6px}
.brand-dot{width:24px;height:24px;border-radius:50%;background:var(--accent)}
.brand-name{font-size:12px;font-weight:700;color:var(--ink);letter-spacing:.2px}
.nav{position:absolute;left:402px;top:0;display:flex;height:40px;font-size:6px;font-weight:700;letter-spacing:.2px}
.nav a{display:flex;align-items:center;height:40px;text-decoration:none;color:var(--ink);margin-right:22px}
.nav a.current{background:var(--accent);color:var(--white);padding:0 9px;margin-right:25px}

/* hero */
.hero{position:absolute;top:62px;left:0;width:684px;height:284px;background:linear-gradient(100deg,#3a4452 0%,#6d7885 35%,#b9c3cc 55%,#4a5260 80%,#2a303a 100%)}
.hero-title{position:absolute;left:66px;top:63px;width:320px;font-size:18.5px;font-weight:700;line-height:21px;color:var(--white)}
.hero-text{position:absolute;left:66px;top:136px;width:240px;font-size:7.4px;line-height:10px;color:var(--white)}
.hero-btn{position:absolute;left:66px;top:179px;width:101px;height:21px;background:var(--green);color:var(--white);font-size:6px;font-weight:700;display:flex;align-items:center;justify-content:center}
.dots{position:absolute;display:flex;gap:4px}
.dots i{width:5px;height:5px;border-radius:50%;background:#c9c9c9;display:block}
.dots i.on{background:var(--white)}
.hero .dots{left:329px;top:262px}

/* sections */
.section-title{position:absolute;left:0;width:684px;text-align:center;font-size:18.5px;font-weight:300;color:var(--ink)}
.section-sub{position:absolute;left:0;width:684px;text-align:center;font-size:11px;font-weight:300;color:var(--teal-muted)}

.services{position:absolute;top:346px;left:0;width:684px;height:240px;background:var(--panel)}
.service{position:absolute;top:92px;width:142px;text-align:center}
.service + .service{border-left:1px solid var(--line)}
.service-icon{width:34px;height:34px;border-radius:50%;background:var(--white);margin:0 auto;display:flex;align-items:center;justify-content:center}
.service-icon svg{width:18px;height:18px}
.service h3{font-size:7px;font-weight:600;margin-top:11px}
.service p{font-family:"Open Sans",Arial,sans-serif;font-size:5.6px;line-height:8px;color:var(--muted);margin:9px auto 0;width:120px;height:24px}
.service .more{display:block;font-size:6px;font-weight:700;margin-top:6px;color:var(--ink)}
.service .more.active{color:var(--accent)}

.testimonials{position:absolute;top:587px;left:0;width:684px;height:275px;background:var(--white);border-top:1px solid var(--line);border-bottom:1px solid var(--line)}
.client{position:absolute;top:97px}
.client-photo{position:absolute;left:0;top:0;width:48px;height:50px;background:linear-gradient(160deg,#8d9aa8,#4a5460)}
.client-name{position:absolute;left:0;top:56px;width:60px;font-size:7px;line-height:10px;color:var(--muted)}
.client-social{position:absolute;left:0;top:78px;display:flex;gap:3px}
.client-social i{display:block;width:5px;height:5px;border-radius:50%;background:var(--sky)}
.quote{position:absolute;left:61px;top:0;width:105px;height:114px;background:var(--white);box-shadow:0 0 3px rgba(0,0,0,.18);padding:11px 7px}
.quote h4{font-size:5.8px;font-weight:700;letter-spacing:.2px}
.quote p{font-family:"Open Sans",Arial,sans-serif;font-size:5.4px;line-height:8px;color:var(--muted);margin-top:6px}
.testimonials .dots{left:329px;top:236px}
.testimonials .dots i{background:#cfcfcf}
.testimonials .dots i.on{background:var(--ink)}

.chat{position:absolute;top:863px;left:0;width:684px;height:251px;background:var(--panel)}
.chat-sub{position:absolute;left:0;top:49px;width:684px;text-align:center;font-size:11px;font-weight:300;line-height:14px;color:var(--teal-muted)}
.chat-sub em{font-style:normal;color:var(--sky)}
.chat-icon{position:absolute;left:320px;top:90px;width:44px;height:44px;border-radius:50%;background:#d4d4d4;display:flex;align-items:center;justify-content:center}
.field{position:absolute;height:19px;background:var(--white);border:1px solid #dcdcdc;font-family:"Open Sans",Arial,sans-serif;font-size:6px;color:#555;padding:5px 6px}
.check{position:absolute;left:444px;top:185px;display:flex;gap:5px;align-items:center;font-family:"Open Sans",Arial,sans-serif;font-size:6px;color:#555}
.check i{width:7px;height:7px;border:1px solid #bbb;background:var(--white);display:flex;align-items:center;justify-content:center}
.btn{position:absolute;top:207px;width:80px;height:19px;color:var(--white);font-size:6px;font-weight:700;display:flex;align-items:center;justify-content:center}
.btn-start{left:444px;background:var(--accent)}
.btn-reset{left:539px;background:var(--dark-btn)}

.footer{position:absolute;top:1114px;left:0;width:684px;height:86px;background:var(--footer);text-align:center}
.footer-social{position:absolute;left:272px;top:17px;display:flex;gap:3.5px}
.footer-social i{display:block;width:12px;height:12px;border-radius:50%;background:#4a4a4a}
.footer-links{position:absolute;top:42px;left:0;width:684px;font-size:6.5px;color:#6b6b6b}
.footer-links a{color:#6b6b6b;text-decoration:none;margin:0 3px}
.footer-copy{position:absolute;top:60px;left:0;width:684px;font-size:6px;color:#5a5a5a}
</style>
</head>
<body>

<div class="topbar">
  <span><svg viewBox="0 0 10 10"><rect x="1" y="2" width="8" height="6" fill="none" stroke="#ddd"/><path d="M1 2l4 3 4-3" fill="none" stroke="#ddd"/></svg>EMAIL US ON : hello@qoral.example</span>
  <span class="call"><svg viewBox="0 0 10 10"><path d="M2 1l2 2-1 1.5c.8 1.4 1.6 2.2 3 3L7.5 6l2 2-1.5 1.5C4.5 9 1 5.5.5 2z" fill="#e4401b"/></svg>CALL US ON : (04) -5812 - 7390</span>
  <span><svg viewBox="0 0 10 10"><circle cx="5" cy="3" r="2" fill="none" stroke="#ddd"/><path d="M1 9c0-3 8-3 8 0" fill="none" stroke="#ddd"/></svg>LOGIN</span>
  <span><svg viewBox="0 0 10 10"><rect x="2" y="4.5" width="6" height="4.5" fill="none" stroke="#ddd"/><path d="M3.3 4.5V3a1.7 1.7 0 013.4 0v1.5" fill="none" stroke="#ddd"/></svg>CLICK TO JOIN</span>
  <span><svg viewBox="0 0 10 10"><circle cx="4" cy="4" r="2.8" fill="none" stroke="#ddd"/><path d="M6 6l3 3" stroke="#ddd"/></svg>KEYWORD SEARCH</span>
</div>

<header class="header">
  <div class="brand"><div class="brand-dot"></div><div class="brand-name">Qoral Software Institute</div></div>
  <nav class="nav">
    <a class="current" href="#">HOME</a>
    <a href="#">TRAINING</a>
    <a href="#">SERVICING</a>
    <a href="#">ABOUT</a>
    <a href="#">CONTACT</a>
  </nav>
</header>

<section class="hero" role="img" aria-label="Business team in suits gathered around a presenter pointing at a growth chart on a flip board">
  <h1 class="hero-title">Sed ut perspiciatis unde omnis iste natus error sit voluptatem totam rem aperiam</h1>
  <p class="hero-text">Lorem ipsum dolor sit amet, consectetur adipisicing elit, sed do eiusmod tempor incididunt ut labore et dolore magna aliqua.</p>
  <div class="hero-btn">CONTACT US NOW !</div>
  <div class="dots"><i class="on"></i><i></i><i></i></div>
</section>

<section class="services">
  <h2 class="section-title" style="top:28px">We provide the best services to our users</h2>
  <p class="section-sub" style="top:55px">Lorem ipsum dolor sit amet elit</p>

  <div class="service" style="left:60px">
    <div class="service-icon"><svg viewBox="0 0 20 20"><rect x="6" y="2" width="12" height="8" fill="none" stroke="#222" stroke-width="1.6"/><circle cx="4" cy="8" r="2" fill="#222"/><path d="M1 17v-5h6v5M2 17h16M9 13h7" stroke="#222" stroke-width="1.6" fill="none"/></svg></div>
    <h3>Training</h3>
    <p>We are privileged for being positioned in a region with IT ancestry. Therefore, since we offer courses to fast...</p>
    <span class="more">Read More</span>
  </div>
  <div class="service" style="left:201px">
    <div class="service-icon"><svg viewBox="0 0 20 20" fill="#e4401b"><rect x="3" y="4" width="3.5" height="3.5"/><rect x="8" y="4" width="3.5" height="3.5"/><rect x="13" y="4" width="3.5" height="3.5"/><rect x="3" y="9" width="3.5" height="3.5"/><rect x="8" y="9" width="3.5" height="3.5"/><rect x="13" y="9" width="3.5" height="3.5"/><rect x="3" y="14" width="3.5" height="3.5"/><rect x="8" y="14" width="3.5" height="3.5"/><rect x="13" y="14" width="3.5" height="3.5"/></svg></div>
    <h3>Software Development</h3>
    <p>We invest a lot in quality development coupled with scalability and modern production tools...</p>
    <span class="more active">Read More</span>
  </div>
  <div class="service" style="left:342px">
    <div class="service-icon"><svg viewBox="0 0 20 20" fill="none" stroke="#222" stroke-width="1.4"><path d="M10 5a4 4 0 00-2.5 7.1V14h5v-1.9A4 4 0 0010 5zM8 16h4M10 1v2M3 4l1.5 1.5M17 4l-1.5 1.5M1 10h2M17 10h2"/></svg></div>
    <h3>Consulting</h3>
    <p>We work to improve the bond of the system with the processes of IT implementations always...</p>
    <span class="more">Read More</span>
  </div>
  <div class="service" style="left:484px">
    <div class="service-icon"><svg viewBox="0 0 20 20"><circle cx="10" cy="10" r="5.5" fill="none" stroke="#222" stroke-width="3" stroke-dasharray="2.2 1.6"/><circle cx="10" cy="10" r="2.6" fill="none" stroke="#222" stroke-width="1.6"/><path d="M12 12l5 5" stroke="#222" stroke-width="2"/></svg></div>
    <h3>Course WEB</h3>
    <p>Watch our calendar for more information on the course web , learn how to work the web environment and...</p>
    <span class="more">Read More</span>
  </div>
</section>

<section class="testimonials">
  <h2 class="section-title" style="top:28px">What our clients say</h2>
  <p class="section-sub" style="top:55px">Sed ut perspiciatis unde omnis iste natus error sit voluptatem</p>

  <div class="client" style="left:66px">
    <div class="client-photo" role="img" aria-label="Portrait of client Marcus Reyes"></div>
    <div class="client-name">Marcus Reyes<br>Officer</div>
    <div class="client-social"><i></i><i></i></div>
    <div class="quote"><h4>LOREM IPSUM DOLOR</h4><p>Lorem ipsum dolor sit amet, er veniam, quis nostrud mgana ut aliquip ex ea consectetur at adipis veniam, quis nostrud vel mgana ut icing elit, sd m modo eos et accusamus et iusto odio voluptatum delenti atque omn s dolor repellendus quidem est amet rerum facilis et .</p></div>
  </div>
  <div class="client" style="left:259px">
    <div class="client-photo" role="img" aria-label="Portrait of client Lena Varga" style="background:linear-gradient(160deg,#c9b8a8,#6e5a4c)"></div>
    <div class="client-name">Lena Varga<br>Designer</div>
    <div class="client-social"><i></i><i></i></div>
    <div class="quote"><h4>LOREM IPSUM DOLOR</h4><p>Lorem ipsum dolor sit amet, er veniam, quis nostrud mgana ut aliquip ex ea consectetur at adipis veniam, quis nostrud vel mgana ut icing elit, sd m modo eos et accusamus et iusto odio voluptatum delenti atque omn s dolor repellendus quidem est amet rerum facilis et .</p></div>
  </div>
  <div class="client" style="left:451px">
    <div class="client-photo" role="img" aria-label="Portrait of client Tomas Hale" style="background:linear-gradient(160deg,#b7c2cc,#3c4652)"></div>
    <div class="client-name">Tomas Hale<br>Officer</div>
    <div class="client-social"><i></i><i></i></div>
    <div class="quote"><h4>LOREM IPSUM DOLOR</h4><p>Lorem ipsum dolor sit amet, er veniam, quis nostrud mgana ut aliquip ex ea consectetur at adipis veniam, quis nostrud vel mgana ut icing elit, sd m modo eos et accusamus et iusto odio voluptatum delenti atque omn s dolor repellendus quidem est amet rerum facilis et .</p></div>
  </div>
  <div class="dots"><i class="on"></i><i></i><i></i></div>
</section>

<section class="chat">
  <h2 class="section-title" style="top:22px">Start a live chat !</h2>
  <p class="chat-sub">Contact a Qoral Software Institute <em>today</em><br><em>for a live</em> chat.</p>
  <div class="chat-icon"><svg width="22" height="16" viewBox="0 0 22 16"><rect x="1" y="1" width="20" height="14" fill="#9a9a9a"/><path d="M1 1l10 8 10-8" fill="none" stroke="#d4d4d4" stroke-width="1.5"/></svg></div>
  <div class="field" style="left:66px;top:153px;width:175px">Name</div>
  <div class="field" style="left:256px;top:153px;width:174px">Email Address</div>
  <div class="field" style="left:444px;top:153px;width:175px">Phone Number</div>
  <div class="field" style="left:66px;top:186px;width:364px;height:40px">Message</div>
  <div class="check"><i><svg width="5" height="5" viewBox="0 0 5 5"><path d="M.5 2.5l1.5 1.5L4.5 1" fill="none" stroke="#49b9e0"/></svg></i>Please add me to the QOR mailing list !</div>
  <div class="btn btn-start">START CHATTING</div>
  <div class="btn btn-reset">RESET FORM</div>
</section>

<footer class="footer">
  <div class="footer-social"><i></i><i></i><i></i><i></i><i></i><i></i><i></i><i></i><i></i></div>
  <div class="footer-links"><a href="#">Home</a> <a href="#">About Us</a> <a href="#">Services</a> <a href="#">Traings</a> <a href="#">Locations</a> <a href="#">Contact Us</a></div>
  <div class="footer-copy">© 2014 QOR. All Rights Reserved.</div>
</footer>

</body>
</html>
```